Talents and colours poster for home office

The objective is to illustrate/communicate and remember 5 talents and 4 colours of the personality.

The infographic will be hanged on the wall of an home office. It need to be simple and clear. Illustrations and pictograms can be used. It can be artistic.

Here's the content:

5 talents,scaling in priority from #1 to #5
Ideation / creativity
Winning other over / charisma
Adaptability
Positivity
Empathy

In the files there is a description of what those mean.

You have to include 4 colours, scaling in priority from #1 to #4
Yellow
Green
Red
Blue

I made a sketch just for fun... and to show why I need professionnal skills :)

THX

Industry/Entity Type

Office

Requirements
Should not have
• offensive materials

```html
<!DOCTYPE html>
<html lang="en">
<head>
<meta charset="utf-8">
<title>Talents</title>
<link rel="stylesheet" href="https://fonts.googleapis.com/css2?family=Alfa+Slab+One&display=swap">
<style>
  :root {
    --sky-light: #eceef0;
    --sky-mid: #b9bcc0;
    --sky-dark: #7d8186;
    --disc: #ffffff;
    --disc-edge: #e4e6e8;
    --orange: #f7941d;
    --green: #3f9b3c;
    --red: #e0301e;
    --blue: #1f9ad6;
    --magenta: #e4138d;
    --label: #ffffff;
  }
  html, body {
    margin: 0;
    padding: 0;
    overflow: hidden;
  }
  .poster {
    position: relative;
    width: 847px;
    height: 1200px;
    overflow: hidden;
    background: var(--sky-mid);
  }
  .sky-backdrop {
    position: absolute;
    inset: 0;
    background:
      radial-gradient(ellipse 60% 30% at 30% 18%, rgba(255,255,255,0.85), rgba(255,255,255,0) 70%),
      radial-gradient(ellipse 70% 25% at 80% 85%, rgba(255,255,255,0.7), rgba(255,255,255,0) 70%),
      radial-gradient(ellipse 50% 30% at 15% 90%, rgba(255,255,255,0.5), rgba(255,255,255,0) 70%),
      linear-gradient(180deg, var(--sky-dark) 0%, var(--sky-mid) 40%, var(--sky-light) 70%, var(--sky-mid) 100%);
  }
  .talent-wheel {
    position: absolute;
    inset: 0;
    width: 847px;
    height: 1200px;
  }
  .talent-label {
    font-family: "Alfa Slab One", Georgia, serif;
    fill: var(--label);
    letter-spacing: 1px;
  }
  .wheel-title {
    font-family: "Alfa Slab One", Georgia, serif;
    fill: var(--magenta);
    font-size: 46px;
  }
</style>
</head>
<body>
<main class="poster">
  <div class="sky-backdrop" role="img" aria-label="Soft grey sky with drifting clouds"></div>

  <svg class="talent-wheel" viewBox="0 0 847 1200" xmlns="http://www.w3.org/2000/svg">
    <defs>
      <filter id="disc-shadow" x="-20%" y="-20%" width="140%" height="140%">
        <feDropShadow dx="0" dy="6" stdDeviation="8" flood-color="#000" flood-opacity="0.28"/>
      </filter>
      <radialGradient id="disc-fill" cx="50%" cy="40%" r="60%">
        <stop offset="0%" stop-color="var(--disc)"/>
        <stop offset="100%" stop-color="var(--disc-edge)"/>
      </radialGradient>

      <path id="orange-baseline" d="M423 277 A313 313 0 0 1 736 590"/>
      <path id="green-baseline" d="M423 338 A252 252 0 0 1 445 841"/>
      <path id="red-baseline" d="M423 398 A192 192 0 1 1 271.7 708"/>
      <path id="blue-baseline" d="M423 447 A143 143 0 0 1 546.8 661.5"/>
    </defs>

    <!-- stacked white discs -->
    <g class="discs" filter="url(#disc-shadow)">
      <circle cx="423" cy="590" r="356" fill="url(#disc-fill)"/>
      <circle cx="423" cy="590" r="300" fill="url(#disc-fill)"/>
      <circle cx="423" cy="590" r="232" fill="url(#disc-fill)"/>
      <circle cx="423" cy="590" r="180" fill="url(#disc-fill)"/>
    </g>

    <!-- talent bands -->
    <g class="bands" fill="none" stroke-linecap="butt">
      <path class="band band-ideation" d="M423 265 A325 325 0 0 1 748 590" stroke="var(--orange)" stroke-width="50"/>
      <path class="band band-charisma" d="M423 327 A263 263 0 0 1 446 852" stroke="var(--green)" stroke-width="68"/>
      <path class="band band-adaptability" d="M423 388 A202 202 0 1 1 264 714" stroke="var(--red)" stroke-width="52"/>
      <path class="band band-empathy" d="M423 437 A153 153 0 1 1 290.5 513.5" stroke="var(--blue)" stroke-width="50"/>
    </g>

    <!-- centre disc -->
    <circle class="centre-disc" cx="423" cy="590" r="128" fill="url(#disc-fill)" filter="url(#disc-shadow)"/>

    <!-- labels -->
    <text class="talent-label" font-size="31"><textPath href="#orange-baseline" startOffset="12">IDEATION / CREATIVITY</textPath></text>
    <text class="talent-label" font-size="33"><textPath href="#green-baseline" startOffset="14">WINNING OTHER OVER / CHARISMA</textPath></text>
    <text class="talent-label" font-size="31"><textPath href="#red-baseline" startOffset="14">ADAPTABILITY / POSITIVITY</textPath></text>
    <text class="talent-label" font-size="29"><textPath href="#blue-baseline" startOffset="10">EMPATHY</textPath></text>

    <text class="wheel-title" x="423" y="606" text-anchor="middle">TALENTS</text>
  </svg>
</main>
</body>
</html>
```